Flyer für Zeitarbeitsfirma
Zielgruppe
Wir sind eine Zeitarbeitsfirma in der Pflege! Unsere Kunden sind Krankenhäuser und Pflegeheime
Aufgabenstellung
Wir möchten eine Art Flyer als erste Seite einer Bewerbungsmappe.
Überschrift: Bewerbung als Personaldienstleister
Warum K7-CURANTA?
Wir bieten entscheidende Unterschiede:
1 Tag KOSTENFREI
(Vermindern Sie Ihr Risiko für schlechtes Zeitarbeitspersonal)
5 Tage günstiger Einarbeitungstarif
anschließend erhalten Sie eine Preisgarantie fürs gesamte Jahr
PLUS kostenfreie Übernahme unserer Mitarbeiter
Worauf warten Sie noch?
Wir freuen uns auf eine tolle Zusammenarbeit!
www.zuvikor-7.de

```html
<!DOCTYPE html>
<html lang="de">
<head>
<meta charset="utf-8">
<title>K7-CURANTA – Bewerbung als Personaldienstleister</title>
<link rel="stylesheet" href="https://fonts.googleapis.com/css2?family=Bebas+Neue&family=Montserrat:wght@400;500;700&display=swap">
<style>
  :root {
    --green: #239a3e;
    --grey-text: #6b6566;
    --ink: #1a1a1a;
    --navy: #073540;
    --teal: #157a92;
    --white: #ffffff;
  }
  * { margin: 0; padding: 0; box-sizing: border-box; }
  html, body { width: 848px; height: 1200px; overflow: hidden; background: var(--white); }
  .flyer { position: relative; width: 848px; height: 1200px; font-family: "Montserrat", sans-serif; color: var(--ink); }

  .brand { position: absolute; left: 15px; top: 14px; display: flex; align-items: center; gap: 12px; }
  .brand-dot { width: 92px; height: 92px; border-radius: 50%; background: var(--green); }
  .brand-name { font-weight: 700; font-size: 42px; color: var(--grey-text); letter-spacing: 0.5px; }

  .headline { position: absolute; left: 450px; top: 78px; font-weight: 700; font-size: 28px; line-height: 44px; color: var(--grey-text); }

  .hero { position: absolute; left: 0; top: 179px; width: 848px; height: 408px; }
  .hero svg { position: absolute; inset: 0; }

  .hand-icon { position: absolute; left: 177px; top: 179px; width: 114px; height: 124px; border-radius: 20px; background: rgba(255,255,255,0.18); }

  .slogan { position: absolute; left: 0; width: 464px; text-align: center; color: var(--white); font-weight: 700; font-size: 19px; line-height: 30px; }
  .slogan-main { top: 328px; }
  .slogan-go { top: 418px; }

  .why { position: absolute; left: 43px; top: 504px; font-family: "Bebas Neue", sans-serif; font-weight: 400; font-size: 66px; line-height: 66px; color: var(--white); letter-spacing: 0.5px; white-space: nowrap; transform: scaleX(0.77); transform-origin: left center; }

  .benefits { position: absolute; left: 41px; top: 634px; list-style: none; }
  .benefit { position: absolute; left: 0; display: flex; align-items: center; width: 780px; }
  .benefit svg { width: 77px; height: 77px; flex: none; }
  .benefit span { margin-left: 22px; font-size: 19px; white-space: nowrap; }

  .offers { position: absolute; left: 41px; top: 928px; width: 766px; color: var(--grey-text); font-size: 15px; line-height: 24px; }
  .offers strong { color: var(--green); font-weight: 700; }

  .contact { position: absolute; top: 1024px; font-size: 20px; }
  .contact-row { display: flex; align-items: center; gap: 6px; height: 34px; margin-bottom: 7px; }
  .contact-left { left: 84px; }
  .contact-right { right: 84px; }
  .contact-right .contact-row { justify-content: flex-end; }
  .contact svg { width: 34px; height: 34px; flex: none; }

  .footer-band { position: absolute; left: 0; top: 1147px; width: 848px; height: 53px; background: linear-gradient(180deg, var(--navy), #135d6e); }
</style>
</head>
<body>
<div class="flyer">
  <div class="brand">
    <div class="brand-dot"></div>
    <div class="brand-name">K7-CURANTA</div>
  </div>

  <h1 class="headline">Bewerbung als<br>Personaldienstleister</h1>

  <div class="hero">
    <svg viewBox="0 0 848 408" width="848" height="408">
      <defs>
        <linearGradient id="ringGrad" x1="0" y1="0" x2="0" y2="1">
          <stop offset="0" stop-color="#0b2e3a"/>
          <stop offset="1" stop-color="#157a92"/>
        </linearGradient>
        <radialGradient id="badgeGrad" cx="0.5" cy="0.45" r="0.55">
          <stop offset="0" stop-color="#f7f7f7"/>
          <stop offset="1" stop-color="#b9b9b9"/>
        </radialGradient>
      </defs>
      <path d="M0 0 H445 Q505 0 560 30 V378 Q505 408 445 408 H0 Z" fill="var(--green)"/>
      <path d="M848 0 H775 Q730 0 690 30 V378 Q730 408 775 408 H848 Z" fill="var(--green)"/>
      <circle cx="624" cy="205" r="210" fill="var(--white)"/>
      <circle cx="624" cy="205" r="199" fill="url(#ringGrad)"/>
      <circle cx="624" cy="205" r="194" fill="var(--white)"/>
      <circle cx="624" cy="205" r="187" fill="var(--green)"/>
      <circle cx="624" cy="205" r="180" fill="url(#badgeGrad)" role="img" aria-label="Illustration: Haus mit Pflegekraft und Patient"/>
    </svg>
  </div>

  <div class="hand-icon" role="img" aria-label="Illustration: zeigende Hand"></div>

  <p class="slogan slogan-main">WIR WOLLEN BEWEGEN<br>SEI EIN TEIL DIESER BEWEGUNG</p>
  <p class="slogan slogan-go">LET'S GO !</p>

  <h2 class="why">WARUM K7-CURANTA ?</h2>

  <ul class="benefits">
    <li class="benefit" style="top:0">
      <svg viewBox="0 0 77 77"><circle cx="38.5" cy="38.5" r="38.5" fill="var(--green)"/><path d="M16 38 L31 55 L60 22" fill="none" stroke="var(--white)" stroke-width="8"/></svg>
      <span>Mehr Geld, spürbar weniger Arbeitsbelastung !</span>
    </li>
    <li class="benefit" style="top:92px">
      <svg viewBox="0 0 77 77"><circle cx="38.5" cy="38.5" r="38.5" fill="var(--green)"/><path d="M16 38 L31 55 L60 22" fill="none" stroke="var(--white)" stroke-width="8"/></svg>
      <span>Mehr Sicherheit durch komplett abgesicherten Arbeitsvertrag !</span>
    </li>
    <li class="benefit" style="top:184px">
      <svg viewBox="0 0 77 77"><circle cx="38.5" cy="38.5" r="38.5" fill="var(--green)"/><path d="M16 38 L31 55 L60 22" fill="none" stroke="var(--white)" stroke-width="8"/></svg>
      <span>Mehr Freizeit durch räumlich &amp; zeitlich attraktive Arbeitsmodelle !</span>
    </li>
  </ul>

  <div class="offers">
    <p><strong>1 Tag KOSTENFREI</strong> · <strong>5 Tage</strong> günstiger Einarbeitungstarif · <strong>Preisgarantie</strong> fürs gesamte Jahr</p>
    <p><strong>PLUS</strong> kostenfreie Übernahme unserer Mitarbeiter – Worauf warten Sie noch?</p>
  </div>

  <div class="contact contact-left">
    <div class="contact-row">
      <svg viewBox="0 0 34 34"><circle cx="17" cy="17" r="17" fill="var(--navy)"/><path d="M11 9 L14 9 L15.5 13 L13.5 14.5 Q15 18.5 19.5 20.5 L21 18.5 L25 20 L25 23 Q24 25 21.5 25 Q10 22.5 9 12 Q9 10 11 9 Z" fill="var(--white)"/></svg>
      <span>+123-456-7890</span>
    </div>
    <div class="contact-row">
      <svg viewBox="0 0 34 34"><circle cx="17" cy="17" r="17" fill="var(--navy)"/><rect x="8" y="11" width="18" height="12" fill="none" stroke="var(--white)" stroke-width="1.8"/><path d="M8 11 L17 18 L26 11" fill="none" stroke="var(--white)" stroke-width="1.8"/></svg>
      <span>info@zuvikor-7.de</span>
    </div>
  </div>

  <div class="contact contact-right">
    <div class="contact-row">
      <span>www.zuvikor-7.de</span>
      <svg viewBox="0 0 34 34"><circle cx="17" cy="17" r="17" fill="var(--navy)"/><g fill="none" stroke="var(--white)" stroke-width="1.6"><circle cx="17" cy="17" r="9"/><ellipse cx="17" cy="17" rx="4" ry="9"/><path d="M8 17 H26 M9.5 12.5 H24.5 M9.5 21.5 H24.5"/></g></svg>
    </div>
    <div class="contact-row">
      <span>123 Anywhere St., Any City</span>
      <svg viewBox="0 0 34 34"><circle cx="17" cy="17" r="17" fill="var(--navy)"/><path d="M17 27 Q10 19 10 14.5 A7 7 0 0 1 24 14.5 Q24 19 17 27 Z" fill="var(--white)"/><circle cx="17" cy="14.5" r="2.6" fill="var(--navy)"/></svg>
    </div>
  </div>

  <div class="footer-band"></div>
</div>
</body>
</html>
```